Business and Success Coaching Business Card

Need a business card for my coaching business. I coach small businesses, career professionals and, individuals wanting to unlock their human potential and achieve excellence. At the heart of our methodology is the Shaping Purposeful Action Routines Knowingly (SPARK) approach to formulate empowerment, create principles for success and setting achievable outcomes. I would like something that incorporates our new logo, something clean and sharp with a solid darker, but complementary background, color on the card front. The back should be white where there will be room for three questions

Target Market(s)

People looking to advance and improve themselves through a success coach

Industry/Entity Type

Life Coaching

Contact Information for Business Card

Contact information on card.
Business name on front of card
Questions on back

Font styles to use
Other font styles liked:
• Century Gothic or other Serif style fonts that look similar to Century Gothic

Colors

Designer to choose colors to be used in the design.

Requirements
Must have
• Logo on front of card
• Business name - The Steady Forge
• Contact name - Ted Harlow
• Address - Box 4619, Littleton, CO 80127-4619
• Phone number - 303-555-0147
• Email address - harlow.ted@thesteadyforge.example
• Certifications - ACC, CLCh, PTM, CNLP
• Back of card
• Three questions on the back of the card:
• If you were at your best, what would you do right now?
• What is the decision you have been avoiding?
• What's one action you could take in the next 10 minutes?
Nice to have
• I would like to see a solid color on the front of the card that compliments the logo.
• Back should be white, or could be contrasting, but need to have the three questions.

```html
<!DOCTYPE html>
<html lang="en">
<head>
<meta charset="utf-8">
<title>The Steady Forge – Business Card</title>
<link rel="stylesheet" href="https://fonts.googleapis.com/css2?family=Questrial&display=swap">
<style>
  :root {
    --backdrop: #4a4a8a;
    --navy: #16163f;
    --blue: #0b5aa0;
    --ink-blue: #1c2c6e;
    --white: #ffffff;
    --ink: #111122;
    --card-w: 540px;
    --card-h: 349px;
  }
  * { margin: 0; padding: 0; box-sizing: border-box; }
  html, body {
    width: 1200px;
    height: 656px;
    overflow: hidden;
    background: var(--backdrop);
    font-family: "Questrial", "Century Gothic", sans-serif;
  }
  .stage {
    position: relative;
    width: 1200px;
    height: 656px;
    display: flex;
    gap: 40px;
    align-items: center;
    justify-content: center;
  }
  .card {
    position: relative;
    width: var(--card-w);
    height: var(--card-h);
    overflow: hidden;
    box-shadow: 4px 6px 14px rgba(20, 20, 50, 0.35);
  }
  .card__shapes {
    position: absolute;
    inset: 0;
    width: 100%;
    height: 100%;
  }

  /* Front */
  .card--front { background: var(--navy); color: var(--white); }
  .brand {
    position: absolute;
    top: 68px;
    left: 392px;
    width: 136px;
    text-align: center;
  }
  .brand__mark {
    display: block;
    width: 22px;
    height: 22px;
    margin: 0 auto 8px;
    border-radius: 50%;
    background: var(--ink-blue);
  }
  .brand__name {
    display: block;
    font-size: 14px;
    color: var(--ink-blue);
    white-space: nowrap;
  }
  .brand__tagline {
    display: block;
    margin-top: 2px;
    font-size: 8px;
    color: var(--white);
    white-space: nowrap;
  }
  .holder-name {
    position: absolute;
    left: 24px;
    top: 172px;
    font-size: 35px;
    font-weight: 400;
    letter-spacing: 0.5px;
  }
  .contact {
    position: absolute;
    left: 24px;
    top: 276px;
    font-size: 12.5px;
    line-height: 17px;
    font-style: normal;
  }
  .contact__address { letter-spacing: 1px; }
  .certifications {
    position: absolute;
    left: 381px;
    top: 300px;
    font-size: 12px;
    line-height: 14px;
    color: var(--ink-blue);
  }

  /* Back */
  .card--back { background: var(--white); }
  .questions {
    position: absolute;
    left: 152px;
    top: 124px;
    list-style: none;
    color: var(--ink);
    font-size: 12.5px;
  }
  .questions__item {
    position: relative;
    padding-left: 16px;
    height: 38px;
    white-space: nowrap;
  }
  .questions__item::before {
    content: "";
    position: absolute;
    left: 0;
    top: 5px;
    width: 6px;
    height: 6px;
    background: var(--ink);
  }
  .questions__item--spaced { letter-spacing: 1.6px; }
</style>
</head>
<body>
<main class="stage">

  <section class="card card--front" aria-label="Card front">
    <svg class="card__shapes" viewBox="0 0 540 349" preserveAspectRatio="none" aria-hidden="true">
      <polygon points="401,0 540,0 540,349 269,349" fill="var(--blue)"/>
    </svg>
    <div class="brand">
      <span class="brand__mark"></span>
      <span class="brand__name">The Steady Forge</span>
      <span class="brand__tagline">Shape your next great step</span>
    </div>
    <h1 class="holder-name">Ted Harlow</h1>
    <address class="contact">
      <div class="contact__address">Box 4619, Littleton, CO 80127-4619</div>
      <div class="contact__phone">303-555-0147</div>
      <div class="contact__email">harlow.ted@thesteadyforge.example</div>
    </address>
    <div class="certifications">
      Certifications:<br>
      ACC, CLCh, PTM, CNLP
    </div>
  </section>

  <section class="card card--back" aria-label="Card back">
    <svg class="card__shapes" viewBox="0 0 540 349" preserveAspectRatio="none" aria-hidden="true">
      <polygon points="0,0 31,0 185,349 0,349" fill="var(--navy)"/>
      <polygon points="31,0 307,0 104,165" fill="var(--blue)"/>
    </svg>
    <ul class="questions">
      <li class="questions__item">If you were at your best, what would you do right now?</li>
      <li class="questions__item questions__item--spaced">What is the decision you have been avoiding?</li>
      <li class="questions__item">What’s one action you could take in the next 10 minutes?</li>
    </ul>
  </section>

</main>
</body>
</html>
```